Wordpress Design Project (Lanternfield)

We need a wordpress design for an established auction and real estate company based in California. The winning design will incorporate a creative layout, pleasing color scheme and logo in a very professional and clean manner.

Industry/Entity Type

Real Estate

Requirements
Must have
• Client likes the overall look of http://pelkora.com/. Site will use the logo colors and maybe complimentary highlight color. Note from client: "“It's important that the appearance of the site will be unique and easily recognizable. In general try to avoid too many colors especially bright and negative contention colors such as bright red, orange, yellow and such. "

The layout should be close as the mentioned reference site except the slideshow (image attached) should be placed below navigation, perhaps at top of content area for the page. Sidebar widgets will include:
- SMS signup form
- Register to bid call to action (as in reference site)
- Email signup form (with only "enter email" field)
- Blog feature "News & Events"
- Social media icons for facebook, twitter, google+, RSS

Navigation:
1) Home
2) Auctions
3) Online Auctions
4) Past Auctions
5) About Us
6) FAQ
7) Blog
8) Contact Us
Nice to have
• Site will have drop-down menus, idea of these would be nice for any of the primary navigation tabs.
Should not have
• please use no auction gavels in the design

```html
<!DOCTYPE html>
<html lang="en">
<head>
<meta charset="utf-8">
<title>Lanternfield Auctions</title>
<link href="https://fonts.googleapis.com/css2?family=Arimo:wght@400;700&family=Ubuntu:wght@400;500;700&family=Source+Sans+3:ital,wght@0,400;0,600;0,700;1,400&display=swap" rel="stylesheet">
<style>
:root{
  --teal:#1b6f68;
  --teal-dark:#0d5651;
  --teal-deep:#0b4f4a;
  --maroon:#8a3537;
  --maroon-light:#a64b4d;
  --text:#3a3a3a;
  --panel-line:#dcdcdc;
  --footer:#1e1e1e;
}
*{box-sizing:border-box;margin:0;padding:0}
html,body{width:1128px;height:1200px;overflow:hidden}
body{position:relative;background:linear-gradient(#d6d6d6 0,#f3f3f3 140px,#f1f1f1 100%);font-family:Arimo,Arial,sans-serif;color:var(--text)}
.abs{position:absolute}

/* header */
.brand{left:107px;top:40px;width:220px;font-family:Ubuntu,sans-serif;font-weight:700;font-size:27px;line-height:32px;color:var(--teal-dark);display:flex;align-items:center;gap:10px}
.brand-mark{width:16px;height:16px;background:var(--maroon);flex:none}
.follow{left:754px;top:66px;font-weight:700;font-size:18px;color:#2a2a2a}
.social{left:865px;top:51px;display:flex;gap:9px}
.social span{width:38px;height:38px;display:block;border-radius:2px}
.s1{background:#3b5a96}.s2{background:#2fa7d9}.s3{background:#c7402f}.s4{background:#ee7a1a}

/* nav */
.nav{left:103px;top:134px;width:944px;height:48px;border-radius:6px;background:linear-gradient(#23807a,#0f5a55);display:flex;align-items:center;list-style:none;padding:0 14px 0 10px;justify-content:space-between}
.nav li{color:#fff;font-size:14px;padding:0 18px;height:24px;line-height:24px;position:relative;white-space:nowrap}
.nav li+li::before{content:"";position:absolute;left:-1px;top:0;height:24px;border-left:1px solid rgba(255,255,255,.28)}
.nav li.active{background:#0c4c48;height:30px;line-height:30px;padding:0 22px 0 8px}
.nav li.active::before{display:none}
.dropdown{left:494px;top:184px;width:138px;list-style:none;background:rgba(190,118,118,.85);border-radius:0 0 4px 4px}
.dropdown li{height:27px;line-height:27px;padding-left:12px;color:#fff;font-weight:700;font-size:13px;border-bottom:1px solid rgba(255,255,255,.25)}
.dropdown li.on{background:var(--teal-dark)}
.dropdown li:last-child{border:none}

/* sidebar */
.widget{left:105px;width:251px;border-radius:7px}
.sms{top:204px;height:249px;background:linear-gradient(#4a4a4a,#111 70%);border:1px solid #222;color:#fff;padding:12px 14px}
.sms h2{font-family:Ubuntu,sans-serif;font-size:21px;font-weight:500;margin-bottom:22px;letter-spacing:.3px}
.field{display:flex;align-items:center;justify-content:flex-end;margin-bottom:16px;font-size:13px;gap:8px;white-space:nowrap}
.field input{width:145px;height:27px;border:1px solid #ccc;background:#fff;flex:none}
.field .select{width:118px;height:24px;position:relative;border:1px solid #ccc;background:#fff;flex:none}
.field .select::after{content:"";position:absolute;right:4px;top:4px;width:14px;height:14px;border:1px solid #777;background:linear-gradient(#fff,#ddd)}
.field.provider{justify-content:flex-start;margin-left:-3px;gap:6px}
.btn-maroon{display:inline-block;background:linear-gradient(var(--maroon-light),var(--maroon));color:#fff;border-radius:4px;font-family:Ubuntu,sans-serif;font-size:15px;letter-spacing:1px}
.sms .btn-maroon{position:absolute;right:17px;top:202px;width:79px;height:30px;line-height:30px;text-align:center}
.register{top:477px;height:155px;background:linear-gradient(#1f7c75,#0c4f4a);overflow:hidden}
.register-art{position:absolute;left:0;bottom:0;width:165px;height:122px;background:radial-gradient(ellipse at 40% 60%,#d9dcde,#a8b8c0 55%,transparent 75%)}
.register h2{position:absolute;right:17px;top:12px;font-family:Ubuntu,sans-serif;font-weight:700;font-size:21px;color:#fff;letter-spacing:.5px;white-space:nowrap}
.register p{position:absolute;right:18px;top:43px;width:180px;text-align:right;color:#fff;font-size:15px;line-height:19px;letter-spacing:.3px}
.light{background:linear-gradient(#fff,#f2f2f2);border:1px solid #dedede}
.email{top:656px;height:174px;padding:12px 16px}
.widget h3{font-family:Ubuntu,sans-serif;font-weight:500;font-size:21px;color:var(--teal-dark);letter-spacing:.3px}
.email label{display:block;font-size:14px;margin:12px 0 7px 1px;color:#333}
.email .input{height:36px;border:1px solid #d5d5d5;border-radius:5px;background:#fff}
.email .btn-maroon{position:absolute;right:16px;top:120px;width:102px;height:30px;line-height:30px;text-align:center}
.blog{top:849px;height:238px;padding:12px 14px 0 14px}
.blog ul{list-style:none;margin-top:14px}
.blog li{font-size:13.5px;color:#333;height:29px;line-height:29px;border-bottom:1px solid #d6d6d6;width:220px;padding-left:4px;white-space:nowrap}
.blog li:last-child{border:none}
.blog li::before{content:"»";color:#666;font-size:10px;margin-right:7px;position:relative;top:-1px}
.more{font-family:"Source Sans 3",sans-serif;font-style:italic;font-size:12px;color:var(--teal-dark)}
.blog .more{position:absolute;right:23px;top:210px}

/* main */
.main{left:367px;top:203px;width:680px;height:884px;background:#fff;border:1px solid var(--panel-line);border-radius:7px}
.slide{left:375px;top:210px;width:665px;height:247px;border-radius:4px;background:linear-gradient(100deg,#6e4a2c 0%,#b58a5a 18%,#4a3426 35%,#c6a47a 55%,#8b5a32 72%,#3a2a22 100%)}
.welcome{left:378px;top:478px;font-family:"Source Sans 3",sans-serif;font-weight:600;font-size:22px;line-height:26px;color:#1d1d1d;letter-spacing:.2px;white-space:nowrap}
.intro{left:380px;top:510px;width:641px;font-size:12.4px;line-height:19.2px;color:#444;text-align:justify}
.main-more{left:949px;top:617px}
.rule{left:384px;top:643px;width:640px;border-top:1px dotted #c9c9c9}
.section-title{left:385px;top:656px;font-family:"Source Sans 3",sans-serif;font-weight:600;font-size:20px;color:var(--maroon);letter-spacing:.4px;white-space:nowrap}
.band{left:384px;top:694px;width:647px;height:33px;background:var(--teal-deep);border-radius:3px;color:#fff;font-family:"Source Sans 3",sans-serif;font-weight:700;font-size:16px;line-height:33px;padding-left:8px}
.lot-photo{left:388px;top:749px;width:141px;height:94px;border:3px solid #333;background:linear-gradient(#7ea0c4 0,#b8c8d6 35%,#c9cdd0 55%,#707e62 80%,#9a9a88 100%)}
.btn-dark{display:flex;align-items:center;gap:10px;background:linear-gradient(#555,#111 60%);color:#fff;border-radius:5px;border:1px solid #000;font-weight:700;white-space:nowrap}
.details{left:388px;top:857px;width:143px;height:31px;padding-left:18px;font-family:"Source Sans 3",sans-serif;font-size:17px}
.lot{left:549px;top:746px;width:490px;font-size:13px;color:#333;line-height:17.5px;letter-spacing:.3px}
.lot h4{font-family:"Source Sans 3",sans-serif;font-weight:600;font-size:17.5px;line-height:22px;color:var(--maroon);margin-bottom:5px;white-space:nowrap}
.lot h5{font-family:"Source Sans 3",sans-serif;font-weight:600;font-size:17px;color:var(--teal-dark);margin:10px 0 5px}
.bid{left:550px;top:937px;width:346px;height:39px;padding-left:10px;gap:13px;font-size:16px;letter-spacing:.3px}

/* footer */
.footer{left:0;top:1124px;width:1128px;height:76px;background:var(--footer)}
.footer-links{left:104px;top:1144px;color:#fff;font-size:12px;display:flex;white-space:nowrap}
.footer-links span+span::before{content:"|";margin:0 9px}
.copy{left:104px;top:1170px;color:#fff;font-size:12px;white-space:nowrap}
.footer-brand{left:935px;top:1152px;font-family:Ubuntu,sans-serif;font-weight:700;font-size:16px;color:#2b8c84;display:flex;align-items:center;gap:7px}
.footer-brand i{width:10px;height:10px;background:#2b8c84;display:block}
</style>
</head>
<body>

<header>
  <div class="abs brand"><span class="brand-mark"></span><span>Lanternfield<br>Auctions</span></div>
  <div class="abs follow">Follow Us:</div>
  <div class="abs social" aria-label="Social media links">
    <span class="s1" role="img" aria-label="Social link 1"></span>
    <span class="s2" role="img" aria-label="Social link 2"></span>
    <span class="s3" role="img" aria-label="Social link 3"></span>
    <span class="s4" role="img" aria-label="News feed"></span>
  </div>
  <ul class="abs nav">
    <li>HOME</li><li>AUCTIONS</li><li>ONLINE AUCTIONS</li><li class="active">PAST AUCTIONS</li><li>ABOUT US</li><li>FAQ</li><li>BLOG</li><li>CONTACT US</li>
  </ul>
</header>

<aside>
  <div class="abs widget sms">
    <h2>SMS Sign-up</h2>
    <div class="field">Your Name: <input type="text" aria-label="Your name"></div>
    <div class="field">Mobile No: <input type="text" aria-label="Mobile number"></div>
    <div class="field provider">Service provider: <span class="select"></span></div>
    <span class="btn-maroon">Signup</span>
  </div>

  <div class="abs widget register">
    <div class="register-art" role="img" aria-label="Illustration of a woman working at a laptop"></div>
    <h2>REGISTER TO BID</h2>
    <p>Click here to find great deals at our online auctions</p>
  </div>

  <div class="abs widget light email">
    <h3>Email Sign-up</h3>
    <label>Enter Email</label>
    <div class="input"></div>
    <span class="btn-maroon">SUBSCRIBE</span>
  </div>

  <div class="abs widget light blog">
    <h3>Blog Feature</h3>
    <ul>
      <li>Live Online Auctions experienced</li>
      <li>Online Auctions experienced</li>
      <li>Live Online Auctions experienced</li>
      <li>Online Auctions experienced</li>
      <li>Live Online Auctions experienced</li>
    </ul>
    <span class="more">More Details ››</span>
  </div>
</aside>

<main>
  <div class="abs main"></div>
  <div class="abs slide" role="img" aria-label="Slideshow photo of an antiques room with china cabinets, glassware and sunflowers"></div>
  <ul class="abs dropdown">
    <li>Past Auction 1</li><li class="on">Past Auction 2</li><li>Past Auction 3</li><li>Past Auction 4</li>
  </ul>
  <h1 class="abs welcome">WELCOME TO LANTERNFIELD AUCTIONS</h1>
  <p class="abs intro">simply dummy text of the printing and typesetting industry. Lorem Ipsum has been the industry's standard dummy text ever since the 1500s, when an unknown printer took a galley of type and scrambled it to make a type speci men book. It has survived not only five centuries, but also a galley of type and scrambled &nbsp;the leap into electronic typesetting, remaining essen tially unchanged. It was popularised in the 1960s with the release of Dryline sheets containing Lorem Ipsum passages.</p>
  <span class="abs more main-more">More Details ››</span>
  <div class="abs rule"></div>
  <h2 class="abs section-title">Live &amp; Online Auctions Scroll Down</h2>
  <div class="abs band">MERCER PHYSICAL THERAPY IN ASHBY, GA</div>

  <div class="abs lot-photo" role="img" aria-label="Photo of a silver minivan for auction"></div>
  <div class="abs btn-dark details">
    <svg width="22" height="22" viewBox="0 0 22 22" aria-hidden="true"><circle cx="13" cy="9" r="6.5" fill="none" stroke="#fff" stroke-width="2.4"/><path d="M8.5 13.5 3 19" stroke="#fff" stroke-width="3.2" stroke-linecap="round"/><path d="M13 6v6M10 9h6" stroke="#fff" stroke-width="1.8"/></svg>
    DETAILS
  </div>

  <div class="abs lot">
    <h4>Dale Harwick Auctions, LLC GAL 4812 - Everything high bidder.</h4>
    <b>Location:</b><br>
    Location 1 - 412 Orchard Hill Rd<br>
    Location 2 - 18 Creekside Ln # 3<br>
    Ashby, GA 30599
    <h5>Online Bidding Only</h5>
    <b>Began:</b>&nbsp; Friday, May 24, 2013 at 10:06 AM EDT<br>
    <b>Ends:</b>&nbsp; Wednesday, June 05, 2013 at 10:00 AM EDT
  </div>

  <div class="abs btn-dark bid">
    <svg width="30" height="26" viewBox="0 0 30 26" aria-hidden="true"><rect x="2" y="1" width="26" height="17" rx="1" fill="#cfd8d6"/><rect x="4" y="3" width="22" height="13" fill="#2d9a6a"/><rect x="12" y="18" width="6" height="4" fill="#bbb"/><rect x="6" y="22" width="18" height="3" fill="#ddd"/></svg>
    Click here for Online Bidding
  </div>
</main>

<footer>
  <div class="abs footer"></div>
  <div class="abs footer-links">
    <span>Home</span><span>Auctions</span><span>Online Auctions</span><span>Past Auctions</span><span>About Us</span><span>FAQ</span><span>Blog</span><span>Contact Us</span>
  </div>
  <div class="abs copy">Copyright (C) Lanternfield Auctions. 2013. &nbsp;All Rights Reserved</div>
  <div class="abs footer-brand"><i></i>Lanternfield</div>
</footer>

</body>
</html>
```